Stationary Design for Norvath Digital

We are after a full stationary back business cards, letterheads, compliment slip, invoice template, delivery note and anything else we could use within the stationary pack.

We would also like an email footer creating.

Our company details to be included on all stationary:

Registered Name: Norvath Limited
Company Registration Number: 20473915
Website: www.norvathdigital.example
email: info@norvathdigital.example
Phone: 01632 960 417
Address: 48 Tamsin Lane Loughborough Leicestershire United Kingdom LE11 9QX

```html
<!DOCTYPE html>
<html lang="en">
<head>
<meta charset="utf-8">
<title>Norvath Digital — Stationery</title>
<link href="https://fonts.googleapis.com/css2?family=Open+Sans:wght@400;600&display=swap" rel="stylesheet">
<style>
  :root {
    --navy: #0d3a6e;
    --slate: #a0a4b0;
    --paper: #ffffff;
    --ink: #4a4a4a;
    --rule: #9a9a9a;
    --gold: #d4a64a;
    --ghost: #d4d6da;
    --shadow: 0 6px 10px rgba(0,0,0,0.28);
  }
  * { margin: 0; padding: 0; box-sizing: border-box; }
  html, body { width: 1200px; height: 1107px; overflow: hidden; background: #ffffff; }
  body { position: relative; font-family: "Open Sans", Arial, sans-serif; color: var(--ink); }
  address { font-style: normal; }

  .sheet { position: absolute; background: var(--paper); box-shadow: var(--shadow); }
  .wordmark { font-family: "Open Sans", Arial, sans-serif; font-weight: 600; color: var(--navy); white-space: nowrap; letter-spacing: 0.02em; }

  /* Letterhead */
  .letterhead { left: 69px; top: 76px; width: 461px; height: 651px; border: 1px solid #cfcfcf; }
  .letterhead .wordmark { position: absolute; left: 51px; top: 40px; font-size: 12px; }
  .letterhead .sender { position: absolute; right: 30px; top: 27px; text-align: right; font-size: 7px; line-height: 9.5px; }
  .letterhead .rule { position: absolute; left: 55px; top: 94px; width: 380px; height: 1px; background: var(--rule); }
  .letterhead .recipient { position: absolute; left: 58px; top: 137px; font-size: 6.6px; line-height: 15.8px; }
  .letterhead .body { position: absolute; left: 58px; top: 245px; width: 362px; font-size: 6.6px; line-height: 15.3px; text-align: justify; letter-spacing: 0.1px; }

  /* Folder */
  .folder { left: 666px; top: 76px; width: 461px; height: 651px; background: var(--slate); }
  .folder .wordmark { position: absolute; left: 0; right: 0; top: 286px; text-align: center; color: #ffffff; font-size: 24px; }

  /* Business cards */
  .card-front { left: 69px; top: 827px; width: 247px; height: 142px; border: 1px solid #d6d6d6; }
  .card-front .wordmark { position: absolute; left: 18px; top: 18px; font-size: 9px; }
  .card-front .person { position: absolute; right: 12px; top: 31px; text-align: right; }
  .card-front .person-name { font-size: 8px; letter-spacing: 0.08em; color: #333; }
  .card-front .person-role { font-size: 4.5px; color: #777; margin-top: 1px; }
  .card-front .contacts { position: absolute; right: 12px; top: 89px; list-style: none; text-align: right; font-size: 6px; line-height: 8.5px; color: var(--navy); }
  .card-front .contacts li::after { content: ""; display: inline-block; width: 4px; height: 4px; border-radius: 50%; background: var(--gold); margin-left: 5px; vertical-align: middle; }
  .card-front .reg { position: absolute; left: 10px; top: 107px; font-size: 6px; color: var(--navy); }
  .card-front .band { position: absolute; left: 0; right: 0; bottom: 0; height: 14px; background: var(--navy); color: #ffffff; font-size: 5.3px; line-height: 14px; padding-left: 9px; white-space: nowrap; }

  .card-back { left: 346px; top: 827px; width: 245px; height: 142px; background: var(--navy); }
  .card-back .wordmark { position: absolute; left: 0; right: 0; top: 54px; text-align: center; color: #ffffff; font-size: 11px; }

  /* Envelope */
  .envelope { left: 635px; top: 770px; width: 523px; height: 234px; background: transparent; box-shadow: none; }
  .envelope .flap { position: absolute; left: 0; top: 0; width: 523px; height: 40px; }
  .envelope .face { position: absolute; left: 0; top: 38px; width: 523px; height: 196px; background: var(--paper); border: 1px solid #d0d0d0; box-shadow: var(--shadow); }
  .envelope .wordmark { position: absolute; left: 28px; top: 28px; font-size: 10px; }
  .envelope .address { position: absolute; left: 34px; top: 130px; font-size: 6.5px; line-height: 8.5px; }
  .envelope .ghost { position: absolute; right: 46px; top: 64px; font-size: 22px; color: var(--ghost); }
</style>
</head>
<body>

  <section class="sheet letterhead">
    <div class="wordmark">Norvath Digital</div>
    <address class="sender">
      48 Tamsin Lane Harrowmere<br>
      Westbridgeshire United Kingdom<br>
      HM4 9QX<br>
      01632 960 417
    </address>
    <div class="rule"></div>
    <div class="recipient">
      Mara Quell<br>Title<br>Company Name<br>4321 First Street<br>Anytown, State ZIP<br>Date 1/30/12
    </div>
    <div class="body">
      Dear Mara,<br>
      Lorem ipsum dolor sit amet, consectetur adipiscing elit, sed do eiusmod tempor incidunt et labore et dolore magna aliquam. Ut enim ad minim veniam, quis nostrud exerc. Irure dolor in reprehend incididunt ut labore et dolore magna aliqua. Ut enim ad minim is nostrud exercitation ullam mmodo consequet. Duis aute in voluptate velit esse cillum dolore eu fugiat nulla pariatur.<br>
      At vver eos et accusam dignissum qui blandit est praesent. Mara quell beynocguon doas nog apoply su trenz ucu hugh rasoluguon monugor or trenz ucugwo jag scannar. Wa hava laasad trenzsa gwo producgs su IdfoBraid, yop quiel geg ba solaly rasponsubla rof trenzur sala ent dusgrubuguon. Offoctivo immoriatoly, hawrgaxeeis phat eit sakem eit vory gast te Piok peish ba useing phen roxas. Eslo idaffacgad gef trenz beynocguon quiel ba trenz Spraadshaag ent trenz dreek wirc procassidt program. Cak pwico vux bolug incluros all uf cak siructor hawrgasi itoms alung gith cakiw nog pwicos.<br>
      Piloaso mako nuto uf cakso dodtos anr koop a cupy uf cak vux noaw yerw phuno. Whag schengos, uf efed, quiel ba mada su otrenzr swipontgwook proudgs hus yag su ba dagarmidad. Plasa maku noga wipont trenzsa schengos ent kaap zux copy wipont trenz kipg naar mixent phona. Cak pwico siructiun ruos nust apoply tyu cak UCU sisulutiun munityaw uw.<br>
      Sincerely yours,<br><br>
      Name Here
    </div>
  </section>

  <section class="sheet folder">
    <div class="wordmark">Norvath Digital</div>
  </section>

  <section class="sheet card-front">
    <div class="wordmark">Norvath Digital</div>
    <div class="person">
      <div class="person-name">ELIAS R. HARTWELL</div>
      <div class="person-role">Chief Financial Officer</div>
    </div>
    <ul class="contacts">
      <li>01632 960 417</li>
      <li>www.norvathdigital.example</li>
      <li>info@norvathdigital.example</li>
    </ul>
    <div class="reg">Reg. No: 20473915</div>
    <div class="band">48 Tamsin Lane Harrowmere Westbridgeshire United Kingdom HM4 9QX</div>
  </section>

  <section class="sheet card-back">
    <div class="wordmark">Norvath Digital</div>
  </section>

  <section class="sheet envelope">
    <svg class="flap" viewBox="0 0 523 40" aria-hidden="true">
      <polygon points="19,0 505,0 523,40 0,40" fill="var(--navy)"/>
    </svg>
    <div class="face">
      <div class="wordmark">Norvath Digital</div>
      <address class="address">
        48 Tamsin Lane Harrowmere<br>
        Westbridgeshire United Kingdom<br>
        HM4 9QX
      </address>
      <div class="wordmark ghost">Norvath Digital</div>
    </div>
  </section>

</body>
</html>
```